I need a powerpoint template for VELMaRKO
INTernational ConsoRtium of Primary Care BIg Data Researchers
Studying the Pandemic Impact on Primary Care Around the World
We are a newly developed consortium/organization. We are family physician big data researchers, we are not for profit, academics. We are clinicians, academics and researchers, currently from 9 different countries around the world (see attached posters). Attached is our logo in various formats our web address is www.velmarkoprimarycare.org. I would like a power point template to use for both internal and external presentations when presenting our work, typically for academic presentations

Target Market(s)

other physicians, academics, policy makers

Font styles to use
Serif
Sans Serif

Colors
0555a3
abd037

Requirements
Must have
• I am trying to project international, primary care, big data research
would like a who we are slide with a map of the world and the following countries
Canada, Australia, China, Norway, Singapore, South Korea, Sweden, UK, US
this map must be editable so that I can add and remove countries over time
we need templates for tables and figures
Nice to have
• would like to incorporate the color scheme of our logo which is
PMS288 for the blue and I'm trying to find out the green code
Should not have
• Don't want it to look like a pharmaceutical company

```html
<!DOCTYPE html>
<html lang="en">
<head>
<meta charset="utf-8">
<title>VELMaRKO Presentation Template</title>
<link href="https://fonts.googleapis.com/css2?family=Oswald:wght@400;500;600&family=Roboto:wght@400;500;700&display=swap" rel="stylesheet">
<style>
:root{
  --blue:#0555a3;
  --navy:#1b2f6b;
  --green:#8db82b;
  --orange:#f6a81c;
  --grey-strip:#e9ebee;
  --page-grey:#a9b0b6;
  --text:#3c3c3c;
  --red:#d0202e;
  --pink:#d81b7f;
}
*{margin:0;padding:0;box-sizing:border-box}
html,body{width:1200px;height:1097px;overflow:hidden;background:#fff}
body{position:relative;font-family:"Roboto",Arial,sans-serif;color:var(--text)}
.slide{position:absolute;width:496px;height:279px;background:#fff;overflow:hidden;box-shadow:0 6px 22px rgba(0,0,0,.14)}
.abs{position:absolute}
.brand{position:absolute;display:flex;align-items:center;gap:3px;font-family:"Roboto",sans-serif;font-weight:700;color:var(--blue);white-space:nowrap}
.brand .dot{border-radius:50%;background:var(--green);flex:none}
.header-brand{left:10px;top:31px;font-size:7px}
.header-brand .dot{width:5px;height:5px}
.header-rule{position:absolute;left:62px;top:18px;width:1px;height:26px;background:#d6d9dc}
.header-title{position:absolute;left:71px;top:21px;font-family:"Oswald",sans-serif;font-weight:500;font-size:6.6px;color:var(--navy);white-space:nowrap}
.header-sub{position:absolute;left:71px;top:31px;font-family:"Oswald",sans-serif;font-weight:500;font-size:5.8px;color:var(--green);white-space:nowrap}
.page-no{position:absolute;right:30px;top:0;width:22px;height:33px;background:var(--page-grey);color:#fff;font-family:"Oswald",sans-serif;font-size:14px;display:flex;align-items:flex-end;justify-content:center;padding-bottom:3px}
.left-strip{position:absolute;left:0;top:109px;width:17px;bottom:0;background:var(--grey-strip)}
.section-block{position:absolute;left:0;top:66px;width:57px;height:43px;color:#fff;font-family:"Oswald",sans-serif;font-weight:500;font-size:38px;line-height:43px;text-align:right;padding-right:6px}
.section-title{position:absolute;left:61px;font-family:"Oswald",sans-serif;font-weight:500;color:var(--green);font-size:18px;line-height:19px}
.body-copy{position:absolute;font-size:4px;line-height:7.4px;text-align:justify;color:#444}
.map-fill{position:absolute}
.callout{position:absolute;border-left:2px solid var(--red);padding-left:8px;font-family:"Oswald",sans-serif;font-size:5.6px;line-height:8px}
.legend{position:absolute;font-size:4.4px;color:#333}
.legend-bar{position:absolute;height:3px}

/* cover */
.cover-globe{left:0;top:0;width:200px;height:279px;background:radial-gradient(circle at 60% 48%,#eef1f4 0,#dde3e9 55%,#f4f6f8 75%,#fff 100%)}
.cover-band{left:0;top:67px;width:496px;height:178px;background:repeating-linear-gradient(180deg,#eef2f6 0 2px,#f8fafc 2px 4px)}
.cover-title{position:absolute;right:142px;text-align:right;font-family:"Oswald",sans-serif;font-weight:600;color:var(--navy);line-height:1}
.cover-sub{position:absolute;right:142px;top:168px;font-family:"Oswald",sans-serif;font-weight:500;color:var(--green);font-size:15.5px}
.cover-rule{position:absolute;left:372px;top:112px;width:2px;height:120px;background:var(--green)}
.cover-url{position:absolute;right:146px;top:226px;font-size:6.4px;font-weight:700;color:var(--green)}
.cover-year{position:absolute;left:390px;top:214px;font-family:"Oswald",sans-serif;font-weight:500;font-size:17px;color:var(--green)}
.cover-brand{left:386px;top:158px;font-size:15px}
.cover-brand .dot{width:9px;height:9px}
.cover-tag{position:absolute;left:388px;top:180px;width:92px;font-size:3.8px;font-weight:700;letter-spacing:.2px;color:var(--green);line-height:5px}

/* who we are */
.hub{position:absolute;left:282px;top:126px;width:74px;height:74px;border-radius:50%;background:#fff;box-shadow:0 0 0 5px #eef1f4,0 3px 10px rgba(0,0,0,.15);display:flex;align-items:center;justify-content:center}
.hub .brand{position:static;font-size:7.5px}
.hub .brand .dot{width:5px;height:5px}
.pill{position:absolute;width:80px;height:14px;border-radius:7px;color:#fff;font-size:4.6px;font-weight:700;line-height:4.8px;display:flex;align-items:center;justify-content:center;text-align:center;padding:0 10px;text-transform:uppercase}
.pill::after{content:"";position:absolute;right:3px;top:3px;width:8px;height:8px;border-radius:50%;background:rgba(255,255,255,.35)}
.pill.right::after{left:3px;right:auto}
.members{position:absolute;font-size:4.6px;font-weight:700;line-height:6px;color:#222;border-bottom:1px solid #ccd;padding-bottom:2px}

/* population */
.country{position:absolute;width:42px;text-align:center}
.country .flag{height:25px}
.country .label{height:11px;color:#fff;font-family:"Oswald",sans-serif;font-size:5.6px;line-height:11px}
.country .num{margin-top:4px;font-family:"Oswald",sans-serif;font-weight:500;font-size:18px;line-height:18px;color:#7d8b96}
.country .unit{font-family:"Oswald",sans-serif;font-size:6px;color:#7d8b96;line-height:7px}
.country .desc{margin-top:3px;font-size:4.2px;line-height:5px;color:#98a3ab}
.country .bar{margin-top:6px;height:4px}
</style>
</head>
<body>

<section class="slide" style="left:79px;top:80px">
  <div class="abs cover-band"></div>
  <div class="abs cover-globe" role="img" aria-label="Faint striped globe with virus particles"></div>
  <h1 class="cover-title" style="top:112px;font-size:24px">STUDYING</h1>
  <h1 class="cover-title" style="top:140px;font-size:24px">THE PANDEMIC IMPACT</h1>
  <p class="cover-sub">on Primary Care Around the World</p>
  <p class="cover-url">www.velmarkoprimarycare.org</p>
  <div class="cover-rule"></div>
  <div class="brand cover-brand"><span class="dot"></span>VELMaRKO</div>
  <p class="cover-tag">GLOBAL ALLIANCE OF PRIMARY CARE DATA ANALYSTS AND MODELERS</p>
  <p class="cover-year">2021</p>
</section>

<section class="slide" style="left:618px;top:81px">
  <div class="brand header-brand"><span class="dot"></span>VELMaRKO</div>
  <div class="header-rule"></div>
  <p class="header-title">Global Alliance of Primary Care Data Analysts and Modelers</p>
  <p class="header-sub">Studying the Pandemic Impact on Primary Care Around the World</p>
  <div class="page-no">2</div>
  <div class="left-strip"></div>
  <div class="section-block" style="background:var(--orange)">1</div>
  <h2 class="section-title" style="top:72px">WHO<br>ARE WE</h2>
  <p class="body-copy" style="left:60px;top:138px;width:107px">Our alliance brings together family physicians, academics and data scientists who study routinely collected primary care records. Members share methods, compare findings across health systems and publish together. This slide introduces each partner site, its lead researchers and the role it plays within the network. Partner sites can be added or removed as the alliance grows over time.</p>
  <div class="map-fill" style="left:200px;top:62px;width:296px;height:200px;background:radial-gradient(ellipse at 50% 50%,#eceff2 0,#f3f5f7 60%,#fff 100%)" role="img" aria-label="Light grey world map behind partner network"></div>
  <svg class="abs" style="left:0;top:0" width="496" height="279" aria-hidden="true">
    <g fill="none" stroke="#9aa4ad" stroke-width=".6" stroke-dasharray="1.5 1.5">
      <path d="M285 73 H309 V122"/><path d="M357 73 H333 V122"/>
      <path d="M264 124 H290 V138"/><path d="M376 104 H349 V132"/>
      <path d="M386 140 H360 V152"/><path d="M386 173 H360"/>
      <path d="M264 188 H290 V178"/><path d="M376 203 H349 V190"/>
      <path d="M285 235 H309 V204"/><path d="M357 235 H333 V204"/>
    </g>
  </svg>
  <div class="hub"><div class="brand"><span class="dot"></span>VELMaRKO</div></div>

  <div class="pill" style="left:205px;top:66px;background:#f6b219">Lakeshore University</div>
  <div class="members" style="left:207px;top:83px;width:76px;display:flex;justify-content:space-between;text-align:right"><span>Ra M<br>Lowe P<br>Fenwick A<br>Hollis T</span><span>Bo L<br>Darcy F<br>Marlow G<br>Pryce H</span></div>
  <div class="pill right" style="left:357px;top:66px;background:#8db82b">Kingsbridge University</div>
  <div class="members" style="left:362px;top:84px">van Ostend R</div>
  <div class="pill right" style="left:376px;top:97px;background:#4fb47f">Harbourview University</div>
  <div class="members" style="left:389px;top:115px">Lam KYT</div>
  <div class="pill" style="left:184px;top:117px;background:#ef7d18">Southbank University</div>
  <div class="members" style="left:203px;top:134px;text-align:right">Corrin D<br>Tarrant-Holloway S</div>
  <div class="pill right" style="left:386px;top:133px;background:#3bb7c7">Hanbit University</div>
  <div class="members" style="left:397px;top:150px">Seo M K</div>
  <div class="pill right" style="left:386px;top:166px;background:#2196d3">Nordfjell Institute of Public Health</div>
  <div class="members" style="left:397px;top:182px">Brekke A L</div>
  <div class="pill" style="left:184px;top:181px;background:#e06a2c">Straits National University</div>
  <div class="members" style="left:230px;top:198px;text-align:right">Tan W Q<br>Lin Y H</div>
  <div class="pill right" style="left:376px;top:196px;background:#1d6fb0">FJORA Nordic Research Centre</div>
  <div class="members" style="left:389px;top:213px">Aaslund RT</div>
  <div class="pill" style="left:205px;top:228px;background:#d23241">PRIMENet</div>
  <div class="members" style="left:255px;top:245px">Morrow J</div>
  <div class="pill right" style="left:357px;top:228px;background:#173e63">Region Solvik</div>
  <div class="members" style="left:365px;top:245px">Lindqvist E M</div>
</section>

<section class="slide" style="left:77px;top:397px">
  <div class="brand header-brand"><span class="dot"></span>VELMaRKO</div>
  <div class="header-rule"></div>
  <p class="header-title">Global Alliance of Primary Care Data Analysts and Modelers</p>
  <p class="header-sub">Studying the Pandemic Impact on Primary Care Around the World</p>
  <div class="page-no">3</div>
  <div class="left-strip"></div>
  <div class="section-block" style="background:var(--green)">2</div>
  <h2 class="section-title" style="top:83px">CONTEXT</h2>
  <p class="body-copy" style="left:60px;top:138px;width:107px;text-align:left">On March 11, 2020 COVID-19 was declared a pandemic by the Global Health Council (GHC). Government responses to the pandemic have varied by country, with respect to the speed, timing and extent to which public health interventions have been instituted</p>
  <div class="callout" style="left:61px;top:193px;color:var(--red)">Cases of COVID-19 have varied by country<br>Cumulative confirmed COVID-19 cases, oct 21, 2020</div>
  <p class="body-copy" style="left:72px;top:211px;width:96px">The number of confirmed cases is lower than the number of actual cases; the main reason for that is limited testing.<br><b>Source</b>: Global Disease Monitor - Situation Update Worldwide - Last updated 23 October, 10:05 (London time)</p>
  <div class="map-fill" style="left:180px;top:70px;width:312px;height:158px;background:linear-gradient(135deg,#8e0f16 0%,#b2181f 35%,#d63a2a 60%,#8e0f16 100%);border-radius:40px 60px 30px 50px;opacity:.92" role="img" aria-label="World choropleth map of cumulative confirmed COVID-19 cases by country, shaded in reds"></div>
  <div class="legend" style="left:210px;top:243px;width:270px;display:flex;justify-content:space-between"><span>No data</span><span>none &nbsp;1</span><span>10</span><span>50</span><span>100</span><span>500</span><span>10,000</span><span>100,000</span><span>500,000</span><span>1 million &gt;5 million</span></div>
  <div class="legend-bar" style="left:210px;top:250px;width:18px;background:#e8e8e8"></div>
  <div class="legend-bar" style="left:232px;top:250px;width:223px;background:linear-gradient(90deg,#4f8a8b 0 10%,#fbd5c5 10% 20%,#f8b39b 20%,#f18a6b 40%,#e0452d 60%,#b51a1f 80%,#6e0a10 100%)"></div>
</section>

<section class="slide" style="left:620px;top:396px">
  <div class="brand header-brand"><span class="dot"></span>VELMaRKO</div>
  <div class="header-rule"></div>
  <p class="header-title">Global Alliance of Primary Care Data Analysts and Modelers</p>
  <p class="header-sub">Studying the Pandemic Impact on Primary Care Around the World</p>
  <div class="page-no">4</div>
  <div class="left-strip"></div>
  <div class="section-block" style="background:var(--green)">2</div>
  <h2 class="section-title" style="top:83px">CONTEXT</h2>
  <div class="callout" style="left:61px;top:138px;color:var(--pink)">Cases of COVID-19 deaths have varied by country<br>Cumulative confirmed COVID-19 cases, Oct 21, 2020</div>
  <p class="body-copy" style="left:72px;top:155px;width:96px">Limited testing and challenges in the attribution of the cause of death means that the number of confirmed death may not be an accurate count of the true number of deaths from COVID-19<br><b>Source</b>: Global Disease Monitor - Situation Update Worldwide - Last updated 23 October, 10:05 (London time)</p>
  <p class="body-copy" style="left:61px;top:222px;width:107px;text-align:left">The unintended consequences on patients and delivery of primary care is anticipated to be varied as well</p>
  <div class="map-fill" style="left:178px;top:70px;width:316px;height:158px;background:linear-gradient(135deg,#8a0a7e 0%,#c02a93 35%,#f08cc0 60%,#d94fa0 80%,#8a0a7e 100%);border-radius:40px 60px 30px 50px;opacity:.9" role="img" aria-label="World choropleth map of cumulative confirmed COVID-19 deaths by country, shaded in pinks and purples"></div>
  <div class="legend" style="left:210px;top:243px;width:276px;display:flex;justify-content:space-between"><span>No data &nbsp;0</span><span>5</span><span>10</span><span>50</span><span>500</span><span>5,000</span><span>10,000</span><span>50,000</span><span>&gt;100,000</span></div>
  <div class="legend-bar" style="left:210px;top:250px;width:18px;background:#e8e8e8"></div>
  <div class="legend-bar" style="left:233px;top:250px;width:222px;background:linear-gradient(90deg,#fde8f1,#f7b6d2 30%,#e869a8 55%,#c41f8a 78%,#6d0a6e)"></div>
</section>

<section class="slide" style="left:79px;top:726px;width:498px;height:280px">
  <div class="brand header-brand"><span class="dot"></span>VELMaRKO</div>
  <div class="header-rule"></div>
  <p class="header-title">Global Alliance of Primary Care Data Analysts and Modelers</p>
  <p class="header-sub">Studying the Pandemic Impact on Primary Care Around the World</p>
  <div class="page-no">7</div>
  <div class="left-strip"></div>
  <div class="section-block" style="background:var(--blue)">4</div>
  <h2 class="section-title" style="top:83px">POPULATION</h2>
  <div class="map-fill" style="left:150px;top:62px;width:340px;height:210px;background:radial-gradient(ellipse at 50% 50%,#edf0f3 0,#f5f7f9 60%,#fff 100%)" role="img" aria-label="Faint world map behind country figures"></div>
  <p class="body-copy" style="left:60px;top:138px;width:107px">Over 85 million patients worldwide<br>Each partner site contributes anonymised electronic medical records drawn from routine primary care. Together these records allow the alliance to compare visit patterns, chronic disease care and prescribing across nine health systems before and during the pandemic period, using shared definitions and methods.</p>

  <div class="country" style="left:195px;top:63px"><div class="flag" style="background:#23357e" role="img" aria-label="Flag of Australia"></div><div class="label" style="background:#a99bd1">AUSTRALIA</div><div class="num">1.1</div><div class="unit">million</div><div class="desc">patients primary<br>care EMR records</div><div class="bar" style="background:#a99bd1"></div></div>
  <div class="country" style="left:252px;top:63px"><div class="flag" style="background:#de2910" role="img" aria-label="Flag of China"></div><div class="label" style="background:#ec8a76">CHINA</div><div class="num">500</div><div class="unit">thousand</div><div class="desc">patients primary<br>care EMR records</div><div class="bar" style="background:#ec8a76"></div></div>
  <div class="country" style="left:310px;top:63px"><div class="flag" style="background:#c4142f" role="img" aria-label="Flag of Norway"></div><div class="label" style="background:#76cbcf">NORWAY</div><div class="num">5</div><div class="unit">million</div><div class="desc">patients primary<br>care EMR records</div><div class="bar" style="background:#76cbcf"></div></div>
  <div class="country" style="left:367px;top:63px"><div class="flag" style="background:linear-gradient(180deg,#ef3340,#f7a0a6)" role="img" aria-label="Flag of Singapore"></div><div class="label" style="background:#bbbbbb">SINGAPORE</div><div class="num">300</div><div class="unit">thousand</div><div class="desc">patients primary<br>care EMR records</div><div class="bar" style="background:#bbbbbb"></div></div>
  <div class="country" style="left:424px;top:63px"><div class="flag" style="background:#f2f2f2;border:1px solid #ddd" role="img" aria-label="Flag of South Korea"></div><div class="label" style="background:#e45562">S KOREA</div><div class="num">50</div><div class="unit">million</div><div class="desc">patients primary<br>care EMR records</div><div class="bar" style="background:#e45562"></div></div>

  <div class="country" style="left:227px;top:165px"><div class="flag" style="background:#1c6aa6" role="img" aria-label="Flag of Sweden"></div><div class="label" style="background:#e3c12f">SWEDEN</div><div class="num">10</div><div class="unit">million</div><div class="desc">patients primary<br>care EMR records</div><div class="bar" style="background:#e3c12f"></div></div>
  <div class="country" style="left:284px;top:165px"><div class="flag" style="background:#1d2f72" role="img" aria-label="Flag of the United Kingdom"></div><div class="label" style="background:#8077b8">UK</div><div class="num">5</div><div class="unit">million</div><div class="desc">patients primary<br>care EMR records</div><div class="bar" style="background:#8077b8"></div></div>
  <div class="country" style="left:343px;top:165px"><div class="flag" style="background:linear-gradient(180deg,#d97a84,#c23a48)" role="img" aria-label="Flag of the United States"></div><div class="label" style="background:#e2553f">US</div><div class="num">3</div><div class="unit">million</div><div class="desc">patients primary<br>care EMR records</div><div class="bar" style="background:#e2553f"></div></div>
  <div class="country" style="left:401px;top:165px"><div class="flag" style="background:#e04a3f" role="img" aria-label="Flag of Canada"></div><div class="label" style="background:#8db82b">CANADA</div><div class="num">600</div><div class="unit">thousand</div><div class="desc">patients primary<br>care EMR records</div><div class="bar" style="background:#8db82b"></div></div>
</section>

</body>
</html>
```